The Pulp Corner- 2026 Menu- Drinks/Food

We are The Pulp Corner, a premium NYC-inspired juice bar.
We need two matching 4K TV menu designs with a clean, modern New York feel.
TV 1 – DRINKS
Cold-Pressed Juices, Smoothies, and Coffee/Espresso.
TV 2 – FOOD
Bowls, Toasts, Wraps, Hot Food, and Treats/Sweets.
The menus should feel bold, minimal, and easy to read from a distance.
Strong typography is preferred over heavy photos. The two screens must clearly match as one brand while serving different purposes.
Designs must be optimized for 4K TVs and in a NYC style (subtle subway / street influence, not cartoonish).
This is what we have now. We are updating items and prices along with changing some items.
I have some changes we’d like to do also. But this is what we are using now

```html
<!DOCTYPE html>
<html lang="en">
<head>
<meta charset="utf-8">
<title>The Pulp Corner Menu</title>
<link href="https://fonts.googleapis.com/css2?family=Inter+Tight:wght@300;400;600;700;800&display=swap" rel="stylesheet">
<style>
:root{
  --stage:#6e6e6e;
  --sand:#ede6d6;
  --paper:#f4f1ec;
  --ink:#1c1c1c;
  --muted:#7a7a7a;
  --rule:#8a857c;
}
*{box-sizing:border-box;margin:0;padding:0}
html,body{width:1073px;height:1200px;overflow:hidden;background:var(--stage);font-family:"Inter Tight",Arial,sans-serif;color:var(--ink)}
.board{position:absolute;left:80px;width:913px;height:514px;background:var(--paper);box-shadow:0 2px 6px rgba(0,0,0,.25);overflow:hidden}
.board--drinks{top:72px}
.board--food{top:614px}
.brand-side{position:absolute;left:0;top:0;width:343px;height:514px;background:var(--sand)}
.title{position:absolute;left:44px;top:48px;font-size:50px;line-height:51px;font-weight:800;letter-spacing:-.055em}
.subtitle{position:absolute;left:44px;top:172px;font-size:28px;line-height:32.5px;font-weight:300;color:var(--muted);letter-spacing:-.01em}
.photo{position:absolute;left:0;width:214px}
.photo--subway{top:303px;height:176px;background:linear-gradient(135deg,#2a2a24 0%,#1c3a2a 45%,#6b5222 70%,#1a1a18 100%)}
.photo--bridge{top:276px;height:203px;background:linear-gradient(110deg,#e9dcb8 0%,#c9a46a 35%,#8a3a22 65%,#5a2418 100%)}
.seal{position:absolute;left:172px;width:80px;height:80px;border-radius:50%;background:var(--paper);border:2px solid #bdb6a8;box-shadow:inset 0 0 0 9px var(--paper),inset 0 0 0 10px #bdb6a8}
.board--drinks .seal{top:349px}
.board--food .seal{top:333px}
.social{position:absolute;left:227px;font-size:10.5px;font-weight:600;color:#5a5a5a;letter-spacing:-.03em;display:flex;align-items:center;gap:5px}
.social::before{content:"";width:10px;height:10px;border:1.2px solid #6a6a6a;border-radius:50%}
.section-head{position:absolute;height:29px;border-bottom:1px solid var(--rule);font-size:18px;line-height:24px;font-weight:700;letter-spacing:-.045em;display:flex;justify-content:space-between;align-items:flex-start}
.section-head svg{width:13px;height:13px;margin-top:6px;margin-right:4px}
.list{position:absolute}
.item{height:38.3px}
.item-name{display:flex;justify-content:space-between;font-size:11.5px;line-height:14px;font-weight:700;letter-spacing:-.04em;text-transform:uppercase}
.item-desc{font-size:11.5px;line-height:15px;font-weight:400;letter-spacing:-.02em}
.tint-box{position:absolute;background:var(--sand)}
.coffee-box{position:absolute;left:635px;top:314px;width:198px;height:152px;border:1px solid #4a4a4a}
.coffee-head{height:37px;border-bottom:1px solid #4a4a4a;padding:0 14px;display:flex;justify-content:space-between;align-items:center;font-size:18px;font-weight:700;letter-spacing:-.045em}
.coffee-head svg{width:13px;height:13px}
.coffee-body{padding:14px 14px 0;font-size:11.5px;line-height:14.7px;letter-spacing:-.03em}
.coffee-body b{font-weight:700}
.row{display:flex;justify-content:space-between;font-weight:700;text-transform:uppercase;width:163px;line-height:16.5px}
.mixins{position:absolute;left:650px;top:187px;width:214px;height:81px;background:var(--sand);padding:10px 15px;font-size:11.5px;line-height:14.6px;letter-spacing:-.03em}
.mixins strong{font-weight:700}
</style>
</head>
<body>

<svg width="0" height="0" style="position:absolute">
  <symbol id="arrow" viewBox="0 0 13 13"><path d="M1 1 L12 12 M12 4 V12 H4" fill="none" stroke="#1c1c1c" stroke-width="1.2"/></symbol>
</svg>

<section class="board board--drinks">
  <div class="brand-side">
    <h1 class="title">The Pulp<br>Corner Menu</h1>
    <p class="subtitle">Cold-Pressed<br>Smoothies<br>Coffee</p>
    <div class="photo photo--subway" role="img" aria-label="Photo of a subway train arriving at a dim underground station platform"></div>
    <div class="seal" role="img" aria-label="Organic badge"></div>
    <p class="social" style="top:449px">@ThePulpCorner212</p>
    <p class="social" style="top:466px">The Pulp Corner</p>
  </div>

  <h2 class="section-head" style="left:377px;top:50px;width:221px">Cold Pressed Juices<svg><use href="#arrow"/></svg></h2>
  <div class="list" style="left:377px;top:87px;width:225px">
    <div class="item"><p class="item-name"><span>Hot Bam</span><span>$12.50</span></p><p class="item-desc">Red apple, lemon, ginger, cayenne</p></div>
    <div class="item"><p class="item-name"><span>Sunset Park</span><span>$12.50</span></p><p class="item-desc">Orange, carrot, celery</p></div>
    <div class="item"><p class="item-name"><span>Lean Green</span><span>$12.50</span></p><p class="item-desc">Spinach, celery, cucumber, romaine, lemon</p></div>
    <div class="item"><p class="item-name"><span>Revive</span><span>$12.50</span></p><p class="item-desc">Cantaloupe, red apple, lemon</p></div>
    <div class="item"><p class="item-name"><span>Glow Up</span><span>$13.00</span></p><p class="item-desc">Celery, lime</p></div>
  </div>

  <h2 class="section-head" style="left:650px;top:50px;width:214px">Smoothies<svg><use href="#arrow"/></svg></h2>
  <div class="list" style="left:650px;top:87px;width:214px">
    <div class="item"><p class="item-name"><span>Spring Street</span><span>$13.00</span></p><p class="item-desc">Coconut water, blueberry, pineapple, spinach</p></div>
    <div class="item"><p class="item-name"><span>Fort Greene</span><span>$13.00</span></p><p class="item-desc">Almond milk, banana, mango, avocado</p></div>
    <div class="item"><p class="item-name"><span>Union Square</span><span>$13.00</span></p><p class="item-desc">Almond milk, açaí, banana, berries</p></div>
    <div class="item"><p class="item-name"><span>The “Cawfee”</span><span>$13.00</span></p><p class="item-desc">Cold brew, almond milk, banana, protein</p></div>
    <div class="item"><p class="item-name"><span>Build Your Own</span><span>$12.00</span></p><p class="item-desc">Base + 3 fruits or veggies</p></div>
  </div>

  <div class="tint-box" style="left:377px;top:287px;width:487px;height:205px"></div>
  <h2 class="section-head" style="left:401px;top:299px;width:182px">Shots<svg><use href="#arrow"/></svg></h2>
  <div class="list" style="left:401px;top:333px;width:181px">
    <div class="item"><p class="item-name"><span>Classic</span><span>$6.00</span></p><p class="item-desc">Ginger, lemon</p></div>
    <div class="item"><p class="item-name"><span>Sunshine</span><span>$6.00</span></p><p class="item-desc">Ginger, lemon, turmeric, black pepper</p></div>
    <div class="item"><p class="item-name"><span>Power Green</span><span>$6.00</span></p><p class="item-desc">Ginger, lemon, cayenne, spinach</p></div>
    <div class="item"><p class="item-name"><span>Detox</span><span>$6.00</span></p><p class="item-desc">Wheatgrass</p></div>
  </div>

  <div class="coffee-box">
    <div class="coffee-head">Cofee &amp; More<svg><use href="#arrow"/></svg></div>
    <div class="coffee-body">
      <p><b>COLD BREW</b></p>
      <p>12 oz <b>$5.50</b> &nbsp;16 oz <b>$7.50</b></p>
      <p>Milk add-ons <b>+$0.75</b></p>
      <p class="row" style="margin-top:6px"><span>Coconut Water</span><span>$5.50</span></p>
      <p class="row"><span>Alkaline Water</span><span>$3.00</span></p>
    </div>
  </div>
</section>

<section class="board board--food">
  <div class="brand-side">
    <h1 class="title">The Pulp<br>Corner Menu</h1>
    <p class="subtitle">Bowls I Toasts<br>Wraps I Treats</p>
    <div class="photo photo--bridge" role="img" aria-label="Photo of a suspension bridge tower beside a red brick building in warm haze"></div>
    <div class="seal" role="img" aria-label="Organic badge"></div>
    <p class="social" style="top:450px">@ThePulpCorner212</p>
    <p class="social" style="top:467px">The Pulp Corner</p>
  </div>

  <h2 class="section-head" style="left:377px;top:50px;width:221px">Bowls<svg><use href="#arrow"/></svg></h2>
  <div class="list" style="left:377px;top:87px;width:225px">
    <div class="item"><p class="item-name"><span>Park Slope</span><span>$13.50</span></p><p class="item-desc">Açaí, granola, banana, honey</p></div>
    <div class="item"><p class="item-name"><span>Bay Ridge</span><span>$14.00</span></p><p class="item-desc">Açaí, granola, banana, berries</p></div>
    <div class="item"><p class="item-name"><span>Bushwick</span><span>$14.25</span></p><p class="item-desc">Açaí, granola, pineapple, coconut</p></div>
    <div class="item"><p class="item-name"><span>The Village</span><span>$14.25</span></p><p class="item-desc">Açaí, mixed fruit, coconut, hemp hearts</p></div>
    <div class="item"><p class="item-name"><span>Build Your Own</span><span>$14.00</span></p><p class="item-desc">Açaí, granola, 2 fruits</p></div>
  </div>

  <h2 class="section-head" style="left:650px;top:50px;width:212px">Parfaits &amp; Treats<svg><use href="#arrow"/></svg></h2>
  <div class="list" style="left:650px;top:87px;width:212px">
    <div class="item"><p class="item-name"><span>Liberty Berry</span><span>$9.00</span></p><p class="item-desc">Yogurt, granola, berries</p></div>
    <div class="item"><p class="item-name"><span>Overnight Oats</span><span>$9.00</span></p><p class="item-desc">Coconut milk, chia, fruit</p></div>
    <div class="item"><p class="item-name"><span>Protein Bites</span><span>$6.25</span></p></div>
  </div>
  <div class="mixins">
    <p><strong>MIX-INS</strong></p>
    <p>(Condensed list, small text)</p>
    <p style="margin-top:2px"><strong>Honey · Granola · Nut Butters<br>Protein · Seeds · Sea Moss</strong></p>
  </div>

  <div class="tint-box" style="left:377px;top:295px;width:487px;height:196px"></div>
  <h2 class="section-head" style="left:401px;top:318px;width:212px">Toasts<svg><use href="#arrow"/></svg></h2>
  <div class="list" style="left:401px;top:355px;width:211px">
    <div class="item"><p class="item-name"><span>The Patriot</span><span>$13.25</span></p><p class="item-desc">Nut butter, berries, honey</p></div>
    <div class="item"><p class="item-name"><span>Avocado Toast</span><span>$14.00</span></p><p class="item-desc">Avocado, everything seasoning</p></div>
    <div class="item"><p class="item-name"><span>Smoked Salmon</span><span>$15.00</span></p><p class="item-desc">Wild salmon, avocado, greens</p></div>
  </div>
  <h2 class="section-head" style="left:649px;top:318px;width:189px">Wraps<svg><use href="#arrow"/></svg></h2>
  <div class="list" style="left:649px;top:357px;width:188px">
    <div class="item"><p class="item-name"><span>Turmeric Chicken</span><span>$15.00</span></p><p class="item-desc">Chicken, greens, balsamic</p></div>
    <div class="item"><p class="item-name"><span>Elite Tuna</span><span>$15.00</span></p><p class="item-desc">Wild tuna, celery, greens</p></div>
    <div class="item"><p class="item-name"><span>Spicy Chickpea (V)</span><span>$14.00</span></p><p class="item-desc">Chickpeas, hummus, sriracha</p></div>
  </div>
</section>

</body>
</html>
```